Harbor Mortgage Relief

Please help us give our website a remake or a FACELIFT. It is not very good but it says what we need it to say. But the design is terrible.
I would like our new design font and logo to be used as the theme.

I also want more photos on the site.

I also want consistency with the pages so they look clean.

We want the professionals to do this, let's see what you got!

Thank you!
Updates

Project Deadline Extended
Reason: I can understand you want to be paid. So I will commit to the fee but I want you to have time to make a KICK ASS website for me dudes! Thanks

HI!  Just wanted to say thanks for your time on these.  A lot are great.  However the firefighters have nothing to do with Foreclosure.  We are saving peoples homes from the bank taking them and selling them.   I LOVE the house photos and the families on the website.  That is the direction we like.  THanks.

THANK U ALL FOR THE WORK!   I like a few ending in the numbers: 147  733  693  536  620  478  727  508     I will go over them and choose one soon.  Thank you.   You will be paid shortly. 

Requirements
Must have
• Bright, Upbeat photos. Color scheme should be in order. We like icons on the bottom. not just text.

```html
<!DOCTYPE html>
<html lang="en">
<head>
<meta charset="utf-8">
<title>Harbor Mortgage Relief</title>
<link rel="stylesheet" href="https://fonts.googleapis.com/css2?family=Arimo:wght@400;700&family=Open+Sans:wght@700;800&family=Tinos:wght@400;700&display=swap">
<style>
:root{
  --red:#d31f26;
  --red-dark:#a8161c;
  --ink:#1d1d1d;
  --text:#2a2a2a;
  --page:#ecebea;
  --band:#2b2b2b;
  --white:#ffffff;
  --yellow:#e6f020;
  --rule:#b9b9b9;
}
*{box-sizing:border-box;margin:0;padding:0}
html,body{width:1200px;height:1112px;overflow:hidden}
body{position:relative;background:radial-gradient(ellipse at 50% 30%,#f5f4f3 0%,var(--page) 70%,#e2e1df 100%);font-family:"Arimo",Arial,sans-serif;color:var(--text)}
.abs{position:absolute}
.top-line{left:0;top:0;width:1200px;height:4px;background:var(--red)}

/* header */
.brand{left:185px;top:30px;display:flex;align-items:center;gap:14px}
.brand-mark{width:70px;height:70px;border-radius:50%;background:var(--red)}
.brand-name{font-family:"Open Sans",Arial,sans-serif;font-weight:800;font-size:27px;line-height:29px;color:var(--red);text-transform:uppercase;width:240px}
.call{left:796px;top:34px;display:flex;align-items:center;gap:10px}
.call svg{width:34px;height:42px}
.call-label{font-family:"Open Sans",Arial,sans-serif;font-weight:800;font-size:16px;color:var(--ink);letter-spacing:.3px}
.call-number{font-family:"Open Sans",Arial,sans-serif;font-weight:800;font-size:25px;color:var(--red);line-height:28px}

/* nav */
.nav{left:0;top:121px;width:1200px;height:36px;background:linear-gradient(#e0282f,var(--red) 60%,var(--red-dark));border-top:1px solid #f0454b}
.nav ul{list-style:none;display:flex;margin-left:189px;height:100%}
.nav li{font-family:"Open Sans",Arial,sans-serif;font-weight:700;font-size:12px;color:var(--white);display:flex;align-items:center;padding:0 21px;border-right:1px solid #ef5a5f;height:100%}
.nav li.current{background:var(--white);color:var(--ink);height:28px;margin-top:4px;padding:0 20px}

/* hero */
.hero-band{left:0;top:157px;width:1200px;height:253px;background:linear-gradient(#3a3a3a,var(--band) 40%,#1c1c1c)}
.hero{left:189px;top:169px;width:828px;height:225px;border:4px solid var(--white);background:linear-gradient(100deg,#e4e3dc 0%,#cfc9bf 35%,#b98f6e 55%,#7fae52 75%,#5c9a3a 100%);box-shadow:0 2px 6px rgba(0,0,0,.5)}
.hero-offer{right:18px;top:6px;text-align:right;font-family:"Open Sans",Arial,sans-serif;font-weight:800}
.hero-offer .big{font-size:22px;color:var(--red);text-shadow:0 0 3px #fff,0 0 3px #fff,0 0 3px #fff}
.hero-offer .small{font-size:17px;color:var(--yellow);text-shadow:0 1px 2px rgba(0,0,0,.7)}
.hero-caption{left:0;top:167px;width:300px;height:46px;background:linear-gradient(90deg,rgba(30,30,30,.75) 0%,rgba(30,30,30,.65) 75%,rgba(30,30,30,0) 100%);padding:5px 10px;font-family:"Open Sans",Arial,sans-serif;font-weight:700;white-space:nowrap}
.hero-caption .lead{font-size:15px;color:var(--white);line-height:19px}
.hero-caption .sub{font-size:12.5px;color:var(--yellow);line-height:17px}

/* panels */
.panel{background:var(--white);box-shadow:0 1px 5px rgba(0,0,0,.28)}
.ribbon{background:linear-gradient(#e0282f,var(--red-dark));color:var(--white);font-family:"Tinos",serif;font-weight:400;font-size:22px;padding:4px 0 0 30px;height:32px}
.ribbon b{font-weight:700}
.welcome{left:198px;top:436px;width:552px;height:336px}
.welcome-ribbon{left:183px;top:429px;width:583px}
.welcome-copy{left:213px;top:480px;width:524px;font-size:10.3px;line-height:13px;text-align:justify;color:var(--text)}
.welcome-copy p{margin-bottom:11px}
.welcome-copy .narrow{width:307px}
.welcome-photo{left:534px;top:470px;width:195px;height:197px;border:6px solid var(--white);box-shadow:0 1px 5px rgba(0,0,0,.35);background:linear-gradient(160deg,#e8e4dc 0%,#b9b2a4 40%,#6f7b5c 70%,#4a5a3c 100%)}

.testimonials{left:797px;top:436px;width:208px;height:336px}
.testimonials-ribbon{left:783px;top:429px;width:234px;padding-left:22px}
.quote{left:808px;width:188px;font-size:10.6px;line-height:14.4px;text-align:justify;padding-left:17px}
.quote::before{content:"\201C";position:absolute;left:0;top:-6px;font-family:"Tinos",serif;font-size:26px;color:var(--red);font-weight:700}
.quote .who{font-weight:700;margin-top:13px}
.quote-divider{left:800px;top:612px;width:202px;border-top:1px dashed #555}
.quote-clip{left:800px;top:620px;width:202px;height:142px;overflow:hidden}

/* services */
.services{left:198px;top:797px;width:807px;height:263px}
.services-title{left:211px;top:806px;font-family:"Tinos",serif;font-weight:400;font-size:22px;color:var(--red)}
.services-title b{font-weight:700}
.rule{left:211px;width:782px;border-top:3px double var(--rule)}
.card{top:850px;width:180px;height:154px}
.card .photo{height:124px;margin:0 10px;border:5px solid var(--white);box-shadow:0 1px 4px rgba(0,0,0,.35)}
.card .label{position:absolute;left:0;bottom:0;width:100%;height:31px;background:linear-gradient(#e0282f,var(--red-dark));color:var(--white);font-weight:700;font-size:11px;display:flex;align-items:center;justify-content:center}
.view{left:551px;top:1030px;width:101px;height:20px;border-radius:5px;background:linear-gradient(#4a4a4a,#111);color:var(--white);font-weight:700;font-size:11px;display:flex;align-items:center;justify-content:center}

/* footer */
.footer{left:0;top:1078px;width:1200px;height:34px;background:linear-gradient(#e0282f,var(--red-dark))}
.copyright{left:196px;top:1088px;font-weight:700;font-size:10.5px;color:var(--white)}
.follow{left:830px;top:1081px;display:flex;align-items:center;gap:8px;font-family:"Tinos",serif;font-weight:700;font-size:21px;color:var(--white)}
.social{width:21px;height:21px;background:#3f7bd0;border-radius:2px}
.social.alt{background:#5ab0e8}
</style>
</head>
<body>
<div class="abs top-line"></div>

<header>
  <div class="abs brand">
    <span class="brand-mark"></span>
    <span class="brand-name">Harbor Mortgage Relief</span>
  </div>
  <div class="abs call">
    <svg viewBox="0 0 34 42" aria-hidden="true">
      <path d="M6 4c3-2 7 0 8 3l2 6c1 2-1 4-3 5 1 5 4 10 8 13 2-1 4-2 6 0l4 5c2 2 1 5-2 6-6 2-14-3-19-11S2 9 6 4z" fill="var(--red)"/>
      <path d="M3 40h28" stroke="#999" stroke-width="2"/>
    </svg>
    <div>
      <div class="call-label">CALL TOLL FREE NOW</div>
      <div class="call-number">888-555-0142</div>
    </div>
  </div>
</header>

<nav class="abs nav">
  <ul>
    <li class="current">HOME</li>
    <li>ABOUT US</li>
    <li>SERVICES</li>
    <li>CONTACT US</li>
    <li>FINANCING OPTION</li>
  </ul>
</nav>

<section class="abs hero-band"></section>
<section class="abs hero" role="img" aria-label="Smiling family of three in front of their house on a sunny lawn">
  <div class="abs hero-offer">
    <div class="big">NO UPFRONT FEES !</div>
    <div class="small">Free Evaluation</div>
  </div>
  <div class="abs hero-caption">
    <div class="lead">Assisting Home Owners</div>
    <div class="sub">who are in the foreclosure process</div>
  </div>
</section>

<section class="abs panel welcome"></section>
<h2 class="abs ribbon welcome-ribbon"><b>Welcome</b> to Our Site</h2>
<div class="abs welcome-photo" role="img" aria-label="Couple embracing while looking at a house"></div>
<div class="abs welcome-copy">
  <p class="narrow"><b>HARBOR MORTGAGE RELIEF</b> specializes in assisting home-owners who are in FORECLOSURE, by offering solid alternatives to losing your home in a Trustee Sale. Having your home foreclosed on can damage your credit for up to 7 years. Most foreclosures end with the home owner being evicted from their home, leaving them with no money, no place to live and without ample time to safely remove their possessions from their home. There is no need to have this happen to you. No matter what part of foreclosure process you are in, WE CAN HELP!</p>
  <p class="narrow">If you have received a Notice of Default (NOD) or Notice of Trustee Sale (NTS), you have options. Contact us today to speak to one of our licensed specialist, and let us help you put this situation behind you.</p>
  <p>We speak to hundreds of homeowners every day, we understand how frustrating this can be. Don't live in fear of what is to come. You have other options, please call or email us today and we will immediately put our specialist to work finding you a solution.</p>
  <p>Don't try to handle this frustrating situation by yourself. HARBOR MORTGAGE RELIEF is a team of knowledgeable real estate professionals, we can offer you a better solution during this tough time.</p>
</div>

<section class="abs panel testimonials"></section>
<h2 class="abs ribbon testimonials-ribbon">Testimonials</h2>
<blockquote class="abs quote" style="top:470px">I'd like to express my gratitude to you and your company and I have to add, for all of the trustworthy and reliable service that you bring to the public. Your company helped put me back together, you in particular are awesome! Thank you again Ray."
  <div class="who">Dorothy</div>
</blockquote>
<div class="abs quote-divider"></div>
<div class="abs quote-clip">
  <blockquote class="abs quote" style="left:8px;top:11px">Harbor Mortgage Relief has been an absolute life saver for me and my family. Their services have changed everything. Instead of my house going into foreclosure and losing everything I own, I now have a chance to start over and the money to do it with! They've been fast, friendly and efficient. I would recommend their services to anyone.</blockquote>
</div>

<section class="abs panel services"></section>
<h2 class="abs services-title"><b>OUR</b> SERVICES</h2>
<div class="abs rule" style="top:836px"></div>
<div class="abs card" style="left:210px">
  <div class="photo" role="img" aria-label="Happy family laughing together at home" style="background:linear-gradient(135deg,#d9c7b0,#b88a68 50%,#e9ddd0)"></div>
  <div class="label">Bringing your mortgage</div>
</div>
<div class="abs card" style="left:412px">
  <div class="photo" role="img" aria-label="Hands holding a small model house" style="background:linear-gradient(135deg,#c79a7a,#e8d8c8 50%,#7f9a6a)"></div>
  <div class="label">HMR can purchase your home</div>
</div>
<div class="abs card" style="left:614px">
  <div class="photo" role="img" aria-label="Banknotes with a pen on a contract" style="background:linear-gradient(135deg,#b8bca0,#8a8c70 50%,#5a4a3a)"></div>
  <div class="label">Financing / Purchase Options</div>
</div>
<div class="abs card" style="left:816px">
  <div class="photo" role="img" aria-label="Renovated entry hall with wooden floor and staircase" style="background:linear-gradient(160deg,#e6dccd,#b48a5c 60%,#6e4526)"></div>
  <div class="label">Remodel your home</div>
</div>
<div class="abs rule" style="top:1018px"></div>
<div class="abs view">View Details</div>

<footer>
  <div class="abs footer"></div>
  <div class="abs copyright">Copyright 2012. HARBORMORTGAGERELIEF.COM. All rights reserved.</div>
  <div class="abs follow">Follow us on <span class="social"></span><span class="social alt"></span></div>
</footer>
</body>
</html>
```